Ecommerce website Home Page Design that is clean and elegant

Design a Home page for an ecommerce website. This website products and offerings will be very similar to :

breezyharborcharms.com
maplecrestbazaar.com

Target Market(s)

Consumer and small shops who can order online.

Industry/Entity Type

Retail

Number of Pages Required

1 page

Colors

Designer to choose colors to be used in the design.

Requirements
Must have
• Exact competition with similar products:
• breezyharborcharms.com
• http://www.maplecrestbazaar.com/
• Home page with featured image banner
• List of items on sale or category based items list
• atleast three banners for sale or shipping related offers.
Nice to have
• The logo has very light colors and products will have lots of colors as you can see on competition sites. So the design must consider this so that logo also stands out somewhat for branding purpose.
Should not have
• Design should not have black background

```html
<!DOCTYPE html>
<html lang="en">
<head>
<meta charset="utf-8">
<title>Festoria – Party Supplies</title>
<link href="https://fonts.googleapis.com/css2?family=Lato:wght@400;700;900&family=Satisfy&display=swap" rel="stylesheet">
<style>
:root{
  --gold:#e8b444;
  --gold-dark:#d9a232;
  --purple:#a98ac0;
  --purple-deep:#9a74b6;
  --price:#a77bc6;
  --ink:#333;
  --muted:#777;
  --line:#e2e2e2;
  --panel:#f1f1f1;
  --cream:#f6ecd6;
  --footer:#e6e6e6;
  --night:#111;
}
*{box-sizing:border-box;margin:0;padding:0}
html,body{width:1200px;height:2439px;overflow:hidden}
body{font-family:"Lato",Arial,sans-serif;color:var(--ink);background:#fff;position:relative}
ul{list-style:none}
.abs{position:absolute}

/* header */
.topbar{left:0;top:0;width:1200px;height:36px;background:var(--gold)}
.brand-tab{left:0;top:0;width:300px;height:98px;background:#fff;border-radius:0 0 0 0}
.brand-tab::after{content:"";position:absolute;right:-22px;top:0;width:44px;height:36px;background:#fff;transform:skewX(35deg)}
.brand{left:48px;top:26px;font-size:44px;font-weight:900;color:var(--purple-deep);letter-spacing:1px}
.search{left:382px;top:5px;width:260px;height:26px;background:#f3cf7c;border-radius:2px;font-size:11px;color:#fff;padding:6px 8px}
.search-btn{right:0;top:0;width:26px;height:26px;background:#f7dc9c;border-radius:0 2px 2px 0}
.toplinks{left:665px;top:0;height:36px;display:flex;gap:26px;align-items:center;font-size:12px;color:#fff}
.mainnav{left:309px;top:50px;display:flex;align-items:center;font-size:12px;color:#333}
.mainnav li{padding:9px 10px}
.mainnav li.active{background:var(--purple);color:#fff;padding:9px 12px}
.caret{font-size:8px;margin-left:3px}

/* hero */
.hero{left:0;top:98px;width:1200px;height:533px;background:linear-gradient(90deg,#050505 0%,#121212 45%,#1c1c1c 100%)}
.hero-art{left:400px;top:98px;width:720px;height:533px;background:radial-gradient(ellipse at 62% 55%,#6b4ea0 0%,#3d2f5c 30%,#1a1a1a 70%,transparent 100%)}
.hero-title{left:161px;top:288px;font-size:32px;font-weight:700;color:#fff;line-height:35px}
.hero-sub{left:161px;top:368px;font-size:16px;font-weight:700;color:#fff}
.btn-gold{background:var(--gold);color:#fff;font-weight:700;font-size:14px;display:flex;align-items:center;justify-content:center;border-radius:2px}
.hero-btn{left:161px;top:403px;width:141px;height:38px}

/* promos */
.promo{top:647px;width:390px;height:260px;overflow:hidden}
.promo-bg{position:absolute;inset:0}
.promo-text{position:absolute;color:#fff}
.btn-purple{background:var(--purple);color:#fff;font-weight:700;font-size:12px;display:inline-flex;align-items:center;justify-content:center;border-radius:2px}

/* sidebar */
.sidebar{left:161px;top:946px;width:228px;height:848px;background:var(--panel);border-bottom:3px solid var(--gold)}
.side-head{height:39px;background:var(--gold);color:#fff;font-size:14px;display:flex;align-items:center;justify-content:space-between;padding:0 12px}
.side-main li{height:37.5px;border-bottom:1px solid var(--line);display:flex;align-items:center;padding:0 12px;font-size:12px;justify-content:space-between;background:#fafafa}
.side-main li.open{background:var(--purple);color:#fff;border:none}
.side-sub li{height:28.5px;display:flex;align-items:center;padding-left:44px;font-size:11px;color:#444;border-bottom:1px solid #e6e6e6}
.side-sub li.group{background:var(--cream);padding-left:44px}
.side-sub li.deep{padding-left:60px}
.side-sub li.deep.active{background:var(--purple);color:#fff;justify-content:space-between;padding-right:12px}
.arr{margin-right:8px}

/* categories */
.cat-title{left:420px;top:944px;font-family:"Satisfy",cursive;font-size:26px;color:#222}
.cat-title::after{content:"";position:absolute;left:0;bottom:-6px;width:60px;height:2px;background:var(--gold)}
.card{width:192px;height:249px;background:#fff;border:1px solid var(--line)}
.card-img{height:174px}
.card-name{text-align:center;font-size:12px;line-height:17px;color:#444;margin-top:10px}
.card-row{position:absolute;left:6px;right:0;bottom:0;height:22px;display:flex;align-items:center;justify-content:space-between}
.price{font-size:15px;color:var(--price)}
.price s{font-size:11px;color:#777;margin-left:3px}
.cart{background:#cfcfcf;color:#333;font-size:10px;font-weight:700;height:22px;padding:0 8px;display:flex;align-items:center}

/* features */
.features{left:0;top:1834px;width:1200px;height:117px;background:var(--gold);display:flex;padding-left:161px;align-items:center;gap:0}
.feature{width:234px;display:flex;align-items:center;gap:10px;color:#fff}
.feature-icon{width:44px;height:44px;border-radius:50%;background:var(--purple);display:flex;align-items:center;justify-content:center;flex:none}
.feature h4{font-size:13px;font-weight:700}
.feature p{font-size:10px}

/* newsletter */
.newsletter{left:0;top:1951px;width:1200px;height:151px;background:#f2f2f2}
.nl-title{left:236px;top:1998px;font-family:"Satisfy",cursive;font-size:22px;color:var(--purple-deep)}
.nl-copy{left:236px;top:2028px;font-size:11px;line-height:14px;color:#444}
.nl-input{left:439px;top:2010px;width:384px;height:36px;background:#fff;border:1px solid #ddd;font-size:12px;padding:10px;color:#555}
.nl-btn{left:831px;top:2010px;width:206px;height:36px}

/* footer */
.footer{left:0;top:2102px;width:1200px;height:277px;background:var(--footer)}
.f-col h5{font-size:13px;font-weight:900;letter-spacing:.5px;color:#222}
.f-col h5::after{content:"";display:block;width:36px;height:2px;background:var(--gold);margin:12px 0 10px}
.f-col li{font-size:11px;line-height:17px;color:#444}
.f-col li::before{content:"›";margin-right:6px}
.f-line{left:322px;top:2290px;width:878px;height:1px;background:#d6d6d6}
.contact{font-size:11px;line-height:17px;color:#444}

/* bottom */
.bottom{left:0;top:2379px;width:1200px;height:60px;background:var(--night)}
.copy{left:161px;top:2402px;font-size:10px;color:#ccc}
.pay{top:2400px;width:32px;height:20px;background:#e8e8e8;border-radius:2px}
.social{top:2392px;width:32px;height:32px;background:#2c2c2c}
.social.first{background:var(--gold)}
</style>
</head>
<body>

<!-- Header -->
<div class="abs topbar"></div>
<div class="abs brand-tab"></div>
<div class="abs brand">Festoria</div>
<div class="abs search">Search Product<div class="abs search-btn"><svg width="26" height="26" viewBox="0 0 26 26"><circle cx="12" cy="12" r="5" fill="none" stroke="#fff" stroke-width="2"/><line x1="16" y1="16" x2="20" y2="20" stroke="#fff" stroke-width="2"/></svg></div></div>
<ul class="abs toplinks">
  <li>$ USD <span class="caret">▼</span></li>
  <li>English <span class="caret">▼</span></li>
  <li>My Account</li>
  <li>♥ My Wishlist</li>
  <li>Login</li>
  <li>0 Items</li>
</ul>
<ul class="abs mainnav">
  <li class="active">Home</li>
  <li>Party Supplies<span class="caret">▼</span></li>
  <li>Occasions &amp; Events<span class="caret">▼</span></li>
  <li>Toys &amp; Games<span class="caret">▼</span></li>
  <li>Crafts<span class="caret">▼</span></li>
  <li>Teacher Supplies<span class="caret">▼</span></li>
  <li>Wedding<span class="caret">▼</span></li>
  <li>Daily Deals<span class="caret">▼</span></li>
  <li>Contact Us</li>
</ul>

<!-- Hero -->
<div class="abs hero"></div>
<div class="abs hero-art" role="img" aria-label="Glow sticks in a jar with party stockings and cat masks"></div>
<h1 class="abs hero-title">Glow Your Party With<br>Our Products</h1>
<p class="abs hero-sub">Party supplies As Per Your Trends</p>
<div class="abs btn-gold hero-btn">SHOP NOW&nbsp;➔</div>
<svg class="abs" style="left:76px;top:322px" width="48" height="86" viewBox="0 0 48 86"><polyline points="44,2 4,43 44,84" fill="none" stroke="#ccc" stroke-width="3"/></svg>
<svg class="abs" style="left:1074px;top:322px" width="48" height="86" viewBox="0 0 48 86"><polyline points="4,2 44,43 4,84" fill="none" stroke="#ccc" stroke-width="3"/></svg>

<!-- Promo banners -->
<div class="abs promo" style="left:0">
  <div class="promo-bg" role="img" aria-label="Woman in a lace masquerade mask with cat masks" style="background:linear-gradient(90deg,#6a4a3a 0%,#2a1e1a 40%,#141010 100%)"></div>
  <div class="promo-text" style="left:148px;top:16px;font-size:14px;font-weight:700">GET YOUR</div>
  <div class="promo-text" style="left:148px;top:40px;font-size:21px;color:var(--gold)">MASK PARTY PROPS</div>
  <div class="promo-text" style="left:148px;top:70px;font-size:21px">10 % OFF</div>
  <div class="promo-text btn-purple" style="left:150px;top:104px;width:90px;height:26px">BUY NOW ➔</div>
</div>
<div class="abs promo" style="left:405px">
  <div class="promo-bg" role="img" aria-label="Legs in patterned Halloween party socks" style="background:linear-gradient(90deg,#c9c2b8 0%,#8a7a6a 35%,#e3a93a 60%,#e8b444 100%)"></div>
  <div class="promo-text" style="right:18px;top:16px;font-size:14px;font-weight:700">GET YOUR</div>
  <div class="promo-text" style="right:18px;top:40px;font-size:21px">HAUNTED PARTY SOCKS</div>
  <div class="promo-text" style="right:18px;top:68px;font-size:26px;color:#222">Only Just $9.00</div>
  <div class="promo-text btn-purple" style="right:18px;top:108px;width:125px;height:30px;font-size:14px">BUY NOW ➔</div>
  <div class="promo-text" style="right:18px;top:206px;font-size:20px">GET FREE SHEPPING</div>
  <div class="promo-text" style="right:18px;top:232px;font-size:10px">*Order over $ 150.00</div>
</div>
<div class="abs promo" style="left:810px">
  <div class="promo-bg" role="img" aria-label="Child wearing colourful party goggles" style="background:linear-gradient(180deg,#c9b3d3 0%,#d9cbe0 50%,#eee7f0 100%)"></div>
  <div class="promo-text" style="left:24px;top:14px;font-size:23px">COOL GOGGLES PARTY</div>
  <div class="promo-text" style="left:24px;top:50px;font-size:21px">20 % OFF</div>
  <div class="promo-text btn-purple" style="left:136px;top:50px;width:100px;height:28px;font-size:13px">BUY NOW ➔</div>
</div>

<!-- Sidebar -->
<aside class="abs sidebar">
  <div class="side-head">CATEGORIES <span>☰</span></div>
  <ul class="side-main">
    <li><span><span class="arr">➔</span>Home</span></li>
    <li><span><span class="arr">➔</span>Party Supplies</span><span class="caret">▼</span></li>
    <li><span><span class="arr">➔</span>Toys &amp; Games</span><span class="caret">▼</span></li>
    <li><span><span class="arr">➔</span>Crafts</span><span class="caret">▼</span></li>
    <li><span><span class="arr">➔</span>Teacher Supplies</span><span class="caret">▼</span></li>
    <li class="open"><span><span class="arr">➔</span>Occasions &amp; Events</span><span class="caret">▲</span></li>
  </ul>
  <ul class="side-sub">
    <li>Birthday Party Supplies</li>
    <li>Baby Shower</li>
    <li>Wedding Party Supplies</li>
    <li>Anniversary</li>
    <li>Bridal Shower</li>
    <li>Grad Events</li>
    <li>Prom &amp; Homecoming</li>
    <li>Graduation Party</li>
    <li>Luau</li>
    <li>Carnival</li>
    <li>Office Parties</li>
    <li class="group">Awareness</li>
    <li class="deep"><span><span class="arr">➔</span>Autism Awareness</span></li>
    <li class="deep"><span><span class="arr">➔</span>Breast Cancer Awareness</span></li>
    <li class="deep active"><span><span class="arr">➔</span>Blue Ribbon Awareness</span><span class="caret">▲</span></li>
    <li class="deep"><span><span class="arr">➔</span>Purple Ribbon Awareness</span></li>
    <li class="deep"><span><span class="arr">➔</span>Red Ribbon Awareness</span></li>
    <li class="deep"><span><span class="arr">➔</span>Shop More......</span></li>
    <li>Religious Items &amp; Celebrations</li>
    <li>Team Spirit Gear</li>
  </ul>
</aside>

<!-- Categories -->
<h2 class="abs cat-title">Shop By Categories</h2>

<div class="abs card" style="left:420px;top:1000px"><div class="card-img" role="img" aria-label="Pink and orange paper fans party decorations" style="background:linear-gradient(135deg,#f06aa0,#f7a23a)"></div><p class="card-name">Party<br>Decorations</p><div class="card-row"><span class="price">$ 190.00<s>$ 390.00</s></span><span class="cart">Add To Cart</span></div></div>
<div class="abs card" style="left:634px;top:1000px"><div class="card-img" role="img" aria-label="Red lace favor gift box" style="background:linear-gradient(135deg,#9a8a80,#c8202a)"></div><p class="card-name">Favors &amp;<br>Gifts</p><div class="card-row"><span class="price">$ 290.00<s>$ 390.00</s></span><span class="cart">Add To Cart</span></div></div>
<div class="abs card" style="left:847px;top:1000px"><div class="card-img" role="img" aria-label="Feathered masquerade masks" style="background:linear-gradient(135deg,#e8e8e8,#c8c0b0)"></div><p class="card-name">Mask&amp;<br>Accessories</p><div class="card-row"><span class="price">$ 150.00<s>$ 390.00</s></span><span class="cart">Add To Cart</span></div></div>

<div class="abs card" style="left:420px;top:1273px"><div class="card-img" role="img" aria-label="Decorated prom venue" style="background:linear-gradient(135deg,#f5d48a,#c89040)"></div><p class="card-name">Prom Themes &amp;<br>Supplies</p><div class="card-row"><span class="price">$ 290.00<s>$ 390.00</s></span><span class="cart">Add To Cart</span></div></div>
<div class="abs card" style="left:634px;top:1273px"><div class="card-img" role="img" aria-label="Christmas tree ornament decoration" style="background:linear-gradient(135deg,#3a7a3a,#c83030)"></div><p class="card-name">Christmas Party Themes<br>&amp; Supplies</p><div class="card-row"><span class="price">$ 390.00<s>$ 890.00</s></span><span class="cart">Add To Cart</span></div></div>
<div class="abs card" style="left:847px;top:1273px"><div class="card-img" role="img" aria-label="Wedding hall with balloon arches" style="background:linear-gradient(135deg,#8a5a3a,#e8d8c8)"></div><p class="card-name">Wedding Themes<br>&amp; Supplies</p><div class="card-row"><span class="price">$ 190.00<s>$ 390.00</s></span><span class="cart">Add To Cart</span></div></div>

<div class="abs card" style="left:420px;top:1545px"><div class="card-img" role="img" aria-label="Assorted boxed gift items" style="background:linear-gradient(135deg,#c8a060,#a02828)"></div><p class="card-name">Assortments<br>Gift</p><div class="card-row"><span class="price">$ 90.00<s>$ 190.00</s></span><span class="cart">Add To Cart</span></div></div>
<div class="abs card" style="left:634px;top:1545px"><div class="card-img" role="img" aria-label="Green plush toys" style="background:linear-gradient(135deg,#d8e8c0,#8ab048)"></div><p class="card-name">Plush<br>Toys</p><div class="card-row"><span class="price">$ 150.00<s>$ 290.00</s></span><span class="cart">Add To Cart</span></div></div>
<div class="abs card" style="left:847px;top:1545px"><div class="card-img" role="img" aria-label="Colourful glow sticks in the dark" style="background:radial-gradient(circle at 50% 55%,#d040c0,#3040a0 45%,#0a0a18 80%)"></div><p class="card-name">Glow<br>Sticks</p><div class="card-row"><span class="price">$ 50.00<s>$ 130.00</s></span><span class="cart">Add To Cart</span></div></div>

<!-- Features -->
<section class="abs features">
  <div class="feature"><div class="feature-icon"><svg width="24" height="24" viewBox="0 0 24 24"><rect x="3" y="7" width="12" height="9" fill="#fff"/><rect x="15" y="10" width="6" height="6" fill="#fff"/><circle cx="7" cy="18" r="2" fill="#fff"/><circle cx="17" cy="18" r="2" fill="#fff"/></svg></div><div><h4>FREE SHIPPING</h4><p>on orders worth $150 or more</p></div></div>
  <div class="feature"><div class="feature-icon"><svg width="24" height="24" viewBox="0 0 24 24"><path d="M8 6h8l3 14H5z" fill="#fff"/><text x="12" y="17" font-size="9" text-anchor="middle" fill="#a98ac0" font-family="Lato,sans-serif">$</text></svg></div><div><h4>WAREHOUSE PRICES</h4><p>with low price guarantee</p></div></div>
  <div class="feature"><div class="feature-icon"><svg width="24" height="24" viewBox="0 0 24 24"><circle cx="12" cy="12" r="9" fill="#fff"/><polyline points="7,12 11,16 17,8" fill="none" stroke="#a98ac0" stroke-width="2.5"/></svg></div><div><h4>LARGEST SELECTION</h4><p>of top quality products</p></div></div>
  <div class="feature"><div class="feature-icon"><svg width="24" height="24" viewBox="0 0 24 24"><path d="M3 5h3l3 10h10l2-7H7" fill="none" stroke="#fff" stroke-width="2"/><circle cx="10" cy="19" r="1.6" fill="#fff"/><circle cx="17" cy="19" r="1.6" fill="#fff"/></svg></div><div><h4>SECURE SHOPPING</h4><p>certified by authorities</p></div></div>
</section>

<!-- Newsletter -->
<div class="abs newsletter"></div>
<svg class="abs" style="left:161px;top:1997px" width="60" height="60" viewBox="0 0 60 60"><polygon points="4,24 30,4 56,24 56,56 4,56" fill="#d39a2e"/><rect x="12" y="12" width="36" height="30" fill="#fff"/><polygon points="4,24 30,42 56,24 56,56 4,56" fill="var(--gold)"/></svg>
<h3 class="abs nl-title">Newsletter Subscribe</h3>
<p class="abs nl-copy">Subscribe to our newsletter for<br>regular updates</p>
<div class="abs nl-input">Enter your e-mail *</div>
<div class="abs btn-gold nl-btn">SUBSCRIBE NOW</div>

<!-- Footer -->
<footer class="abs footer"></footer>
<div class="abs f-col" style="left:161px;top:2147px"><h5>QUICK LINKS</h5><ul><li>Home</li><li>Party Supplies</li><li>Occasions &amp; Events</li><li>Toys &amp; Games</li><li>Crafts</li><li>Teacher Supplies</li><li>Wedding</li><li>Daily Deals</li><li>Contact Us</li></ul></div>
<div class="abs f-col" style="left:322px;top:2147px"><h5>CUSTOMER CARE</h5><ul><li>Shipping Info</li><li>FAQs</li><li>Coupons</li><li>Military Discount</li></ul></div>
<div class="abs f-col" style="left:485px;top:2147px"><h5>PARTY CENTRAL</h5><ul><li>Party Ideas</li><li>Party Planning Help</li><li>Party Videos</li><li>Party Plus: Shipping</li></ul></div>
<div class="abs f-col" style="left:647px;top:2147px"><h5>FESTORIA</h5><ul><li>Wholesale Program</li><li>Careers at Festoria</li><li>Affiliate Program</li><li>Partner With Us</li></ul></div>
<div class="abs f-col" style="left:810px;top:2147px"><h5>ABOUT US</h5><ul><li>Our Story</li><li>Contact Us</li><li>Press Release</li><li>Our Services</li></ul></div>
<div class="abs f-col" style="left:940px;top:2147px"><h5>MY ACCOUNT</h5><ul><li>Order Status</li><li>Log In</li><li>My Wishlist</li></ul></div>
<div class="abs f-line"></div>
<div class="abs f-col" style="left:322px;top:2293px"><h5>CONTACT INFORMATION</h5></div>
<p class="abs contact" style="left:528px;top:2295px">📍 4004 4th Floor Ipsum is simply dummy text of the printing<br>&nbsp;&nbsp;&nbsp;&nbsp;and typesetting -0000 UK</p>
<p class="abs contact" style="left:886px;top:2295px">✆ +0-555-0142-300<br>✉ info@festoria-shop.com</p>

<!-- Bottom bar -->
<div class="abs bottom"></div>
<p class="abs copy">© 2017 Festoria. All Rights Reserved.</p>
<div class="abs pay" style="left:515px"></div>
<div class="abs pay" style="left:550px"></div>
<div class="abs pay" style="left:585px"></div>
<div class="abs pay" style="left:620px"></div>
<div class="abs pay" style="left:655px"></div>
<div class="abs social first" style="left:880px"></div>
<div class="abs social" style="left:933px"></div>
<div class="abs social" style="left:970px"></div>
<div class="abs social" style="left:1007px"></div>

</body>
</html>
```